We are starting a new service that will combine local city menus and specials from local restaurants that will then be emailed and printed out on our website.. its a free service to the subscribers and a small charge to the restaurants. We need something to reflect the restaurant industry and to appeal to the general public alike, free to the end user. They sign up and receive daily specials in an email from our site.. not just one city but any one they pick that we service.. We would need links to include. Home, About Us, Sign Up (for free to public), Add Your Restaurant (increase sales and reduce daily calls).. and Contact Us link.. the name of the service is Town Plates at the Ready and website will be townplatesattheready.example. thank you

```html
<!DOCTYPE html>
<html lang="en">
<head>
<meta charset="utf-8">
<title>Town Plates at the Ready</title>
<link href="https://fonts.googleapis.com/css2?family=Lobster&family=Roboto+Condensed:wght@400;700&family=PT+Sans&display=swap" rel="stylesheet">
<style>
:root{
  --red:#d40000;
  --dark:#1b1b1b;
  --ink:#222;
  --grey-band:#efefef;
  --white:#fff;
  --muted:#cccccc;
  --caption:rgba(0,0,0,.55);
}
*{box-sizing:border-box;margin:0;padding:0}
html,body{width:904px;height:1200px;overflow:hidden;background:var(--white)}
body{position:relative;font-family:"PT Sans",sans-serif;color:var(--ink)}
a{color:inherit;text-decoration:none}
.abs{position:absolute}
.cond{font-family:"Roboto Condensed",sans-serif}
.script{font-family:"Lobster",cursive}

.site-header{left:0;top:0;width:904px;height:60px;background:var(--dark);border-top:2px solid var(--red)}
.brand{left:88px;top:14px;color:var(--white);font-size:22px;font-family:"Roboto Condensed",sans-serif;white-space:nowrap}
.phone-tab{left:692px;top:0;width:123px;height:22px;background:var(--red);border-radius:0 0 5px 5px;color:var(--white);font-size:12px;display:flex;align-items:center;justify-content:center;gap:5px;font-family:"Roboto Condensed",sans-serif}
.main-nav{top:34px;right:89px;display:flex;gap:18px;font-size:13px;font-family:"Lobster",cursive;white-space:nowrap}
.main-nav a{color:var(--white)}
.main-nav a.current{color:var(--red)}

.hero{left:0;top:60px;width:904px;height:304px;background:linear-gradient(100deg,#c9b49a 0%,#e9d2a8 30%,#f3dfb6 60%,#d6b58d 100%)}
.hero-slide{left:89px;top:76px;width:477px;height:271px;border:2px solid var(--red);background:linear-gradient(135deg,#6b4a32,#9c6a3e 40%,#c78a4c 65%,#e9e3da 100%);overflow:hidden}
.slide-caption{left:0;bottom:0;width:100%;height:36px;background:var(--caption);color:var(--white);font-size:20px;display:flex;align-items:center;justify-content:center}
.slide-arrow{right:10px;top:120px;color:rgba(255,255,255,.7);font-size:26px}
.promo-card{left:586px;top:76px;width:229px;height:271px;background:rgba(255,255,255,.85);text-align:center}
.promo-title{margin-top:12px;color:var(--red);font-weight:700;font-size:26px;line-height:29px}
.promo-text{margin:12px 16px 0;font-size:9.6px;line-height:15.3px;color:#333}
.btn-red{left:27px;top:220px;width:175px;height:35px;background:var(--red);border-radius:4px;color:var(--white);font-size:25px;font-weight:700;display:flex;align-items:center;justify-content:center}

.section-heading{left:0;width:904px;text-align:center;font-size:20px;color:var(--ink)}
.section-heading em{font-style:normal;color:var(--red)}
.tile{width:168px;height:95px;border:1px solid #888;overflow:hidden}
.tile-label{left:0;bottom:0;width:100%;height:23px;background:var(--caption);color:var(--white);font-size:12px;display:flex;align-items:center;justify-content:center}

.steps-band{left:0;top:696px;width:904px;height:230px;background:var(--grey-band)}
.step{width:160px;text-align:center}
.step svg{display:block;margin:0 auto}
.step-label{margin-top:8px;font-size:16.5px;color:var(--ink)}
.btn-dark{left:357px;top:906px;width:220px;height:38px;background:var(--dark);border-radius:5px;color:var(--white);font-size:20px;display:flex;align-items:center;justify-content:center}

.testimonial{left:89px;top:988px;width:726px;height:136px;border:1px solid #e4e4e4;box-shadow:0 2px 3px rgba(0,0,0,.08);background:var(--white)}
.testimonial-photo{left:3px;top:3px;width:212px;height:129px;background:linear-gradient(135deg,#5a3b24,#a27a52 50%,#d8c8b0)}
.quote-mark{color:var(--red);font-family:Georgia,serif;font-size:34px;font-weight:700;line-height:1}
.quote-text{left:271px;top:22px;width:430px;font-size:10px;line-height:15.3px;color:#333}
.client{right:16px;top:105px;font-size:10.5px}

.site-footer{left:0;top:1155px;width:904px;height:45px;background:var(--dark);border-top:3px solid var(--red)}
.footer-links{left:89px;top:10px;color:var(--muted);font-size:8.5px;white-space:nowrap}
.footer-links a{color:var(--muted)}
.footer-copy{left:89px;top:24px;color:var(--muted);font-size:8px}
.follow{left:688px;top:13px;color:var(--white);font-size:11.5px;display:flex;align-items:center;gap:6px}
.social{width:20px;height:20px;background:var(--red);border-radius:2px}
</style>
</head>
<body>

<header class="site-header abs">
  <div class="brand abs">Town Plates at the Ready</div>
  <div class="phone-tab abs">
    <svg width="14" height="14" viewBox="0 0 14 14"><circle cx="7" cy="7" r="6" fill="none" stroke="#fff" stroke-width="1.2"/><path d="M5 3.5c-1 .6-1.3 2-.4 3.8s2.2 2.9 3.5 3c.6 0 1-.4 1.2-.8L8.1 8.3l-.8.6c-.7-.3-1.4-1.2-1.6-2l.6-.7z" fill="#fff"/></svg>
    000 - 0000 - 0000
  </div>
  <nav class="main-nav abs">
    <a class="current" href="#">Home</a><a href="#">About Us</a><a href="#">Sign Up</a><a href="#">Add Your Restaurant</a><a href="#">Contact Us</a>
  </nav>
</header>

<section class="hero abs" role="img" aria-label="Soft blurred restaurant table backdrop"></section>
<div class="hero-slide abs" role="img" aria-label="Plated dish with vegetables, rice and garnish">
  <span class="slide-arrow abs">&#8250;</span>
  <div class="slide-caption abs cond">Lorem Ipsum is simply dummy text</div>
</div>
<div class="promo-card abs">
  <h1 class="promo-title cond">CONTRARY<br>TO<br>POPULAR BELIEF</h1>
  <p class="promo-text">It is a long established fact that a reader will be distracted by the readable content of a page when looking at its layout. The point of using Lorem Ipsum is that it has a more-or-less normal distribution of letters, as opposed to using</p>
  <div class="btn-red abs cond">Sign Up Now</div>
</div>

<h2 class="section-heading abs script" style="top:384px">There are many variations of passages of <em>Lorem Ipsum available</em></h2>

<div class="tile abs" style="left:89px;top:437px;background:linear-gradient(135deg,#5a2a10,#a55a22,#d8a060)" role="img" aria-label="Roast dinner spread"><div class="tile-label abs cond">Plan a dinner</div></div>
<div class="tile abs" style="left:275px;top:437px;background:linear-gradient(135deg,#d8d4cc,#f0eadf,#b0553a)" role="img" aria-label="Breakfast table setting"><div class="tile-label abs cond">Plan a dinner</div></div>
<div class="tile abs" style="left:462px;top:437px;background:linear-gradient(135deg,#8a6a30,#d0a870,#e8dcc0)" role="img" aria-label="Grilled sandwich plate"><div class="tile-label abs cond">Plan a dinner</div></div>
<div class="tile abs" style="left:648px;top:437px;background:linear-gradient(135deg,#2a1a10,#6a3a1a,#a06030)" role="img" aria-label="Restaurant dining room"><div class="tile-label abs cond">Plan a dinner</div></div>
<div class="tile abs" style="left:89px;top:551px;background:linear-gradient(180deg,#e08a3a,#6a4a3a 50%,#2a2a30)" role="img" aria-label="Candlelit seaside dining at sunset"><div class="tile-label abs cond">Plan a dinner</div></div>
<div class="tile abs" style="left:275px;top:551px;background:linear-gradient(135deg,#e8e8e8,#b04a2a,#6a8a3a)" role="img" aria-label="Salmon fillet with green beans"><div class="tile-label abs cond">Plan a dinner</div></div>
<div class="tile abs" style="left:462px;top:551px;background:linear-gradient(135deg,#3a2a1a,#8a4a2a,#c03a2a)" role="img" aria-label="Bartender pouring a drink"><div class="tile-label abs cond">Plan a dinner</div></div>
<div class="tile abs" style="left:648px;top:551px;background:linear-gradient(135deg,#c08a4a,#e8b070,#7a4a20)" role="img" aria-label="Diners sharing a meal"><div class="tile-label abs cond">Plan a dinner</div></div>

<section class="steps-band abs"></section>
<h2 class="section-heading abs script" style="top:712px">Lorem Ipsum is simply dummy text of the printing</h2>

<div class="step abs" style="left:92px;top:768px">
  <svg width="88" height="88" viewBox="0 0 88 88"><circle cx="44" cy="44" r="42" fill="none" stroke="#d40000" stroke-width="2"/><circle cx="44" cy="30" r="13" fill="#d40000"/><path d="M20 80c0-22 10-32 24-32s24 10 24 32z" fill="#d40000"/><circle cx="72" cy="16" r="11" fill="#efefef"/><path d="M72 9v14M65 16h14" stroke="#d40000" stroke-width="4"/></svg>
  <div class="step-label cond">Sign Up With Us</div>
</div>
<div class="step abs" style="left:279px;top:768px">
  <svg width="88" height="88" viewBox="0 0 88 88"><circle cx="44" cy="44" r="42" fill="#d40000"/><circle cx="44" cy="44" r="36" fill="none" stroke="#fff" stroke-width="2"/><rect x="22" y="30" width="44" height="30" fill="#fff"/><path d="M22 30l22 18 22-18M22 60l16-15M66 60L50 45" fill="none" stroke="#d40000" stroke-width="2.5"/></svg>
  <div class="step-label cond">Get Email From Us</div>
</div>
<div class="step abs" style="left:465px;top:768px">
  <svg width="88" height="88" viewBox="0 0 88 88"><circle cx="44" cy="44" r="42" fill="#d40000"/><circle cx="44" cy="44" r="36" fill="none" stroke="#fff" stroke-width="2"/><path d="M28 22h32v46H28z" fill="#fff"/><path d="M44 22v46" stroke="#d40000" stroke-width="2"/><rect x="33" y="36" width="6" height="8" fill="#d40000"/><rect x="49" y="30" width="6" height="8" fill="#d40000"/><rect x="49" y="48" width="6" height="8" fill="#d40000"/></svg>
  <div class="step-label cond">Select Your Menu</div>
</div>
<div class="step abs" style="left:651px;top:768px">
  <svg width="88" height="88" viewBox="0 0 88 88"><circle cx="44" cy="44" r="42" fill="#d40000"/><circle cx="44" cy="44" r="36" fill="none" stroke="#fff" stroke-width="2"/><path d="M24 58a20 20 0 0140 0z" fill="#fff"/><circle cx="44" cy="36" r="3" fill="#fff"/><rect x="20" y="60" width="48" height="4" fill="#fff"/><path d="M37 20c-3 3 3 5 0 9M44 18c-3 3 3 5 0 9M51 20c-3 3 3 5 0 9" fill="none" stroke="#fff" stroke-width="1.5"/></svg>
  <div class="step-label cond">Enjoy Your Food</div>
</div>

<div class="btn-dark abs cond">Sign Up Now</div>

<section class="testimonial abs">
  <div class="testimonial-photo abs" role="img" aria-label="Waiter serving a guest at a restaurant table"></div>
  <span class="quote-mark abs" style="left:247px;top:14px">&ldquo;</span>
  <p class="quote-text abs">Lorem ipsum dolor sit amet, consectetur adipiscing elit. Nulla ornare, nisi ut interdum condimentum, felis lectus pharetra nunc, nec tristique quam mi eu nunc. Nulla ornare sagittis ante, id sollicitudin nunc. Vestibulum ut sodales nisi. Pellentesque nunc dolor, faucibus in erat a, hendrerit mattis elit. Duis ornare mi ut risus egestas malesuada.</p>
  <span class="quote-mark abs" style="left:460px;top:74px">&rdquo;</span>
  <div class="client abs cond">--- Client Name Here</div>
</section>

<footer class="site-footer abs">
  <div class="footer-links abs cond"><a href="#">Home</a> | <a href="#">About Us</a> | <a href="#">Sign Up</a> | <a href="#">Add Your Restaurant</a> | <a href="#">Contact Us</a></div>
  <div class="footer-copy abs cond">Copyright &copy; 2014 Town Plates at the Ready. All rights reserved.</div>
  <div class="follow abs cond">Follow Us -
    <span class="social" aria-label="Social link"></span><span class="social" aria-label="Social link"></span><span class="social" aria-label="Social link"></span>
  </div>
</footer>

</body>
</html>
```